Real Estate Web Design

Hi

We are a real estate agency who is looking for a Corporate Design that would match our Style Guide. We have already developed the website but we want to apply our Branding on top of it. I am looking for some creative concepts

Below is our Test link for our new website
http://brightkeyhomes.sampledemo.com.au/

Attached is our Style Guide

Cheers
Ruvo

Industry/Entity Type

Real Estate

```html
<!DOCTYPE html>
<html lang="en">
<head>
<meta charset="utf-8">
<title>Brightkey Homes</title>
<link href="https://fonts.googleapis.com/css2?family=Arimo:wght@400;700&display=swap" rel="stylesheet">
<style>
:root{
  --ink:#333;
  --muted:#666;
  --blue:#1f5aa6;
  --blue-btn:#1d4f98;
  --link:#6b86c6;
  --red:#e8302a;
  --price:#d9342b;
  --dark:#1c1c1c;
  --darker:#141414;
  --footer:#2b2b2b;
  --panel:#e9e9e9;
  --line:#dcdcdc;
  --social:#6f7f93;
  --white:#fff;
}
*{box-sizing:border-box;margin:0;padding:0}
html,body{width:786px;height:1200px;overflow:hidden;background:var(--white)}
body{font-family:"Arimo",Arial,sans-serif;color:var(--ink);position:relative}
.abs{position:absolute}

/* header */
.topbar{left:0;top:0;width:786px;height:16px;background:var(--darker);color:#bbb;font-size:6px}
.topbar .date{left:112px;top:4px}
.topbar .phone{left:458px;top:3px;font-size:8px;font-weight:700;color:#eee;display:flex;align-items:center;gap:3px;white-space:nowrap}
.topbar .search{left:541px;top:2px;width:132px;height:13px;background:#fff;border-radius:2px;font-size:7px;color:#aaa;padding:2px 5px}
.topbar .search svg{position:absolute;right:4px;top:2px}
.header{left:0;top:16px;width:786px;height:71px;background:linear-gradient(#262626,#161616)}
.brand{left:120px;top:8px;color:var(--white);font-weight:700;font-size:12px;line-height:1.1}
.nav{left:234px;top:0;height:59px;display:flex;font-size:8.5px;font-weight:700;color:var(--white);white-space:nowrap}
.nav a{color:inherit;text-decoration:none;padding:20px 8px 0}
.nav .active{background:var(--red);width:38px;text-align:center;padding:20px 0 0;height:59px;margin-right:6px;clip-path:polygon(0 0,100% 0,100% 88%,50% 100%,0 88%)}

/* hero */
.hero{left:0;top:87px;width:786px;height:222px;background:linear-gradient(100deg,#3a2516 0%,#6e5136 28%,#5f7fa8 48%,#2c4f86 70%,#1f2d44 100%)}
.hero h1{left:115px;top:60px;color:#fff;font-size:22px;font-weight:700}
.hero p{left:115px;top:88px;width:440px;color:#e8e8e8;font-size:8px;line-height:1.35}
.tag{left:515px;top:138px;height:29px;display:flex}
.tag .info{background:rgba(0,0,0,.75);width:110px;padding:4px 7px;color:#fff;font-size:9px;font-weight:700}
.tag .info span{display:block;font-size:6px;font-weight:400;color:#bbb;margin-top:3px}
.tag .price{background:#111;width:46px;color:#fff;font-size:11px;font-weight:700;display:flex;align-items:center;justify-content:center}

/* search */
.finder{left:120px;top:283px;width:538px;height:127px;background:#fff;border:1px solid var(--line);box-shadow:0 1px 3px rgba(0,0,0,.1)}
.tabs{display:flex;height:26px}
.tabs div{flex:1;background:#ececec;border-left:1px solid #ddd;font-size:7px;color:#aaa;text-align:center;line-height:26px}
.tabs .on{background:#fff;color:#444}
.field{position:absolute;height:22px;border:1px solid #ccc;border-radius:2px;font-size:6.5px;color:#aaa;padding:0 6px;line-height:20px;background:#fff}
.field.sel{color:#444}
.field.sel::after{content:"";position:absolute;right:5px;top:8px;border:3px solid transparent;border-top-color:#555}
.go{position:absolute;left:382px;top:72px;width:138px;height:24px;background:var(--blue);color:#fff;font-size:8px;font-weight:700;border-radius:2px;text-align:center;line-height:24px}

/* deals */
.section-title{color:var(--blue);font-size:16px;font-weight:700}
.deals-title{left:0;top:420px;width:786px;text-align:center}
.lead{left:145px;top:444px;width:496px;text-align:center;font-size:7px;color:#555;line-height:1.45}
.deal{top:481px;width:134px;height:147px;background:var(--panel)}
.photo{width:100%}
.deal .photo{height:85px}
.deal h3{font-size:7.5px;font-weight:700;margin:6px 5px 4px}
.deal .rent{font-size:7px;color:var(--price);margin:0 5px 8px}
.deal .spec{font-size:7px;color:#444;margin:0 5px}

/* featured */
.feat-title{left:112px;top:642px;display:flex;align-items:center;width:562px}
.feat-title::after{content:"";flex:1;height:4px;margin-left:10px;border-top:1px solid #ddd;border-bottom:1px solid #ddd}
.feature{top:668px;width:134px}
.feature .photo{height:94px}
.feature h3{font-size:7.5px;color:var(--link);font-weight:700;margin:10px 0 7px}
.feature p{font-size:7px;color:#555;line-height:1.4;height:34px}
.more{display:inline-block;margin-top:4px;background:var(--blue-btn);color:#fff;font-size:7px;font-weight:700;padding:3px 11px}

/* categories */
.cat{top:862px;display:flex;align-items:center;gap:8px}
.cat .badge{width:78px;height:78px;border-radius:50%;background:radial-gradient(#fafafa,#dedede);display:flex;align-items:center;justify-content:center}
.cat .badge div{width:40px;height:40px;border-radius:6px}
.cat small{display:block;font-size:8px;color:#555}
.cat strong{display:block;font-size:15px;color:#333;letter-spacing:.5px}
.cat a{font-size:7.5px;color:var(--blue);text-decoration:none}
.shadowline{left:60px;top:950px;width:666px;height:12px;background:radial-gradient(ellipse at 50% 0,rgba(0,0,0,.25),rgba(0,0,0,0) 70%)}

/* story */
.story{left:118px;top:976px;width:550px;height:57px;background:#f1f1f1}
.story .label{position:absolute;left:10px;top:8px;font-size:9px;color:#555;line-height:1.2;letter-spacing:.3px}
.story .btn{position:absolute;left:9px;top:35px;background:var(--blue-btn);color:#fff;font-size:6.5px;font-weight:700;padding:3px 6px}
.story .quote{position:absolute;left:80px;top:0;width:470px;height:57px;background:#fff;padding:10px 30px;font-size:6.5px;color:#888;line-height:1.5;border-left:1px solid #ddd}
.story .quote .by{position:absolute;right:60px;bottom:6px;color:var(--price);font-style:italic}
.story .quote::before{content:"\201C";position:absolute;left:14px;top:2px;font-size:16px;color:#555}
.story .quote::after{content:"\201D";position:absolute;right:22px;bottom:-2px;font-size:16px;color:#555}

/* footer */
.footer{left:0;top:1045px;width:786px;height:155px;background:var(--footer)}
.footer .rule{position:absolute;left:0;top:35px;width:786px;height:1px;background:#3d3d3d}
.col{position:absolute;top:14px}
.col h4{font-size:9px;color:#ddd;letter-spacing:.5px;font-weight:400}
.col ul{list-style:none;margin-top:22px}
.col li{font-size:7px;color:#ccc;margin-bottom:6px;padding-left:10px;position:relative}
.col li::before{content:"";position:absolute;left:2px;top:3px;width:3px;height:3px;border-radius:50%;background:#aaa}
.thumbs{display:grid;grid-template-columns:repeat(3,34px);gap:3px;margin-top:22px}
.thumbs div{height:17px;background:linear-gradient(#8fa9c4,#6d8a55)}
.thumbs div:nth-child(2n){background:linear-gradient(#a9bed0,#587842)}
.contact{font-size:7px;color:#ccc;margin-top:20px;line-height:1.4}
.contact p{display:flex;gap:6px;align-items:flex-start;margin-bottom:4px}
.socials{display:flex;gap:3px;margin-top:3px}
.socials span{width:10px;height:10px;border-radius:2px;background:var(--social)}
.copy{position:absolute;left:0;bottom:6px;width:786px;text-align:center;font-size:6.5px;color:#999}
</style>
</head>
<body>

<div class="abs topbar">
  <div class="abs date">SATURDAY, November 16, 2013 18:31</div>
  <div class="abs phone">
    <svg width="7" height="7" viewBox="0 0 24 24"><path fill="#ddd" d="M6.6 10.8a15 15 0 0 0 6.6 6.6l2.2-2.2c.3-.3.7-.4 1-.2 1.1.4 2.3.6 3.6.6.6 0 1 .4 1 1V20c0 .6-.4 1-1 1A17 17 0 0 1 3 4c0-.6.4-1 1-1h3.5c.6 0 1 .4 1 1 0 1.3.2 2.5.6 3.6.1.3 0 .7-.2 1z"/></svg>
    08 - 5550 - 4127
  </div>
  <div class="abs search">Search Here
    <svg width="9" height="9" viewBox="0 0 24 24"><circle cx="10" cy="10" r="7" fill="none" stroke="#222" stroke-width="3"/><path d="M15 15l7 7" stroke="#222" stroke-width="3"/></svg>
  </div>
</div>

<header class="abs header">
  <div class="abs brand">Brightkey<br>Homes</div>
  <nav class="abs nav">
    <a class="active" href="#">Home</a>
    <a href="#">About Us</a>
    <a href="#">Land Loards</a>
    <a href="#">Tenants</a>
    <a href="#">Properties</a>
    <a href="#">Contact Us</a>
    <a href="#">Franchise Opportunities</a>
  </nav>
</header>

<section class="abs hero" role="img" aria-label="Photo of a modern bedroom with large windows overlooking city towers">
  <h1 class="abs">214 Larkin Ave</h1>
  <p class="abs">Nulla facilisi. Phasellus ac enim mi. Cras ut tortor sit dui. Nunc consequat erat lacus, in volutpat nisi sodales vitae. Phasellus pharetra at nulla at egestas. Vestibulum sit amet tortor sit amet diam placerat tincidunt sit amet eget lorem. Phasellus posuere posuere felis.</p>
  <div class="abs tag">
    <div class="info">214 Larkin Ave<span>3 Bed Rooms &nbsp;|&nbsp; 2 Bath Rooms</span></div>
    <div class="price">$40000</div>
  </div>
</section>

<section class="abs finder">
  <div class="tabs"><div class="on">FOR SALE</div><div>FOR RENT</div><div>FORECLOSURES</div><div>NEW HOMES</div></div>
  <div class="field" style="left:19px;top:40px;width:388px">eg. street names, local areas, etc</div>
  <div class="field" style="left:414px;top:40px;width:106px">Min. Year</div>
  <div class="field sel" style="left:19px;top:72px;width:73px">Bedrooms</div>
  <div class="field sel" style="left:100px;top:72px;width:73px">Bathrooms</div>
  <div class="field" style="left:182px;top:72px;width:90px">Min. Price</div>
  <div class="field" style="left:281px;top:72px;width:92px">Max. Price</div>
  <div class="go">&#9906; SEARCH PROPERTY</div>
</section>

<h2 class="abs section-title deals-title">We are Offering the Best Real Estate Deals</h2>
<p class="abs lead">For the past 10 years in the South West we have been the leading specialist rental company. We have provided satisfaction to hundred's of landlords by getting the best tenant, paying the best rent in the shortest possible time.</p>

<article class="abs deal" style="left:112px"><div class="photo" role="img" aria-label="Photo of a white villa with a pool" style="background:linear-gradient(#7fb0e0,#d9d3c0 60%,#4d9bc9)"></div><h3>8 Orla Road, Maple Park</h3><div class="rent">$ 270 /month</div><div class="spec">3 Bed| 3 Bath | 4300 Sq Ft</div></article>
<article class="abs deal" style="left:255px"><div class="photo" role="img" aria-label="Photo of a two storey family house" style="background:linear-gradient(#9fc3e6,#b6a88e 60%,#6c8a4a)"></div><h3>35 Fernwood Road, WA 6001</h3><div class="rent">$ 270 /month</div><div class="spec">3 Bed| 3 Bath | 4300 Sq Ft</div></article>
<article class="abs deal" style="left:397px"><div class="photo" role="img" aria-label="Photo of a bright living room with fireplace" style="background:linear-gradient(#e8e4dc,#b9b3a6 60%,#7b6d5a)"></div><h3>15 Hollis Crescent, WA 6002</h3><div class="rent">$ 270 /month</div><div class="spec">3 Bed| 3 Bath | 4300 Sq Ft</div></article>
<article class="abs deal" style="left:540px"><div class="photo" role="img" aria-label="Photo of a white colonial house on a lawn" style="background:linear-gradient(#a8c9e8,#e1e1dc 55%,#5f8c3b)"></div><h3>2/41 Tanner Street, Maple Park</h3><div class="rent">$ 270 /month</div><div class="spec">3 Bed| 3 Bath | 4300 Sq Ft</div></article>

<h2 class="abs section-title feat-title">Featured Properties</h2>

<article class="abs feature" style="left:112px"><div class="photo" role="img" aria-label="Photo of a family home with large shed" style="background:linear-gradient(#a9c8e6,#dcdcd6 55%,#5b8a36)"></div><h3>Eaton with Large Shed</h3><p>This comfortable family home with a large shedworkshop is well positioned close to shopping centres...</p><span class="more">More</span></article>
<article class="abs feature" style="left:255px"><div class="photo" role="img" aria-label="Photo of a modern brick home" style="background:linear-gradient(#b7d2ea,#b9a597 55%,#6a8f45)"></div><h3>18 Heron Turn, Bayview</h3><p>If you dream of a family home focused on space and luxury, you'll love this modern home for modern l...</p><span class="more">More</span></article>
<article class="abs feature" style="left:397px"><div class="photo" role="img" aria-label="Photo of an apartment building lit at night" style="background:linear-gradient(#1d2230,#5a4128 55%,#c98b3a)"></div><h3>Unit 7/18 Castell Blvd Seaview</h3><p>Spacious, stylish furnished apartment in prime location with award winning restaurants and...</p><span class="more">More</span></article>
<article class="abs feature" style="left:540px"><div class="photo" role="img" aria-label="Photo of a green-roofed house on a hill" style="background:linear-gradient(#c7dbe9,#d4dcd2 50%,#4e8a37)"></div><h3>4B Merrow Close, Lakeside</h3><p>Compact 4 bedroom 2 bathroom unit with reverse cycle air conditioning. Features open plan kitchen, m...</p><span class="more">More</span></article>

<div class="abs cat" style="left:112px"><div class="badge"><div role="img" aria-label="Illustration of a house" style="background:linear-gradient(#555,#ddd)"></div></div><div><small>PROPERTIES FOR</small><strong>SALE</strong><a href="#">View all Properties &gt;&gt;</a></div></div>
<div class="abs cat" style="left:305px"><div class="badge"><div role="img" aria-label="Illustration of a brick house" style="background:linear-gradient(#c7935c,#7a4f2c)"></div></div><div><small>PROPERTIES FOR</small><strong>RENT</strong><a href="#">View all Properties &gt;&gt;</a></div></div>
<div class="abs cat" style="left:496px"><div class="badge"><div role="img" aria-label="Illustration of an office building" style="background:linear-gradient(#9ec6e6,#4b7fae)"></div></div><div><small>PROPERTIES FOR</small><strong>LEASE</strong><a href="#">View all Properties &gt;&gt;</a></div></div>

<div class="abs shadowline"></div>

<section class="abs story">
  <div class="label">SUCCESS<br>STORY</div>
  <span class="btn">Read More</span>
  <div class="quote">Lorem Ipsum is simply dummy text of the printing. Lorem Ipsum is simply dummy text of the printing. Lorem Ipsum is simply dummy text of the printing. Lorem Ipsum is simply dummy text of the printing. Lorem Ipsum is simply dummy text of the printing. Lorem Ipsum is simply dummy text of the printing.<span class="by">----Mara</span></div>
</section>

<footer class="abs footer">
  <div class="rule"></div>
  <div class="col" style="left:114px"><h4>PROPERTIES</h4><ul><li>Villas for Sale</li><li>Apartments for Rent</li><li>Office Space</li><li>Search one</li><li>Latest offers</li></ul></div>
  <div class="col" style="left:255px"><h4>ABOUT US</h4><ul><li>Why Real Estate?</li><li>Our Experience</li><li>Our Expertise</li><li>Our Location</li><li>Get in touch</li></ul></div>
  <div class="col" style="left:396px"><h4>GALLERY</h4>
    <div class="thumbs" role="img" aria-label="Gallery of house photos"><div></div><div></div><div></div><div></div><div></div><div></div></div>
  </div>
  <div class="col" style="left:535px"><h4>CONTACT US</h4>
    <div class="contact">
      <p><svg width="7" height="7" viewBox="0 0 24 24"><path fill="#ccc" d="M6.6 10.8a15 15 0 0 0 6.6 6.6l2.2-2.2c.3-.3.7-.4 1-.2 1.1.4 2.3.6 3.6.6.6 0 1 .4 1 1V20c0 .6-.4 1-1 1A17 17 0 0 1 3 4c0-.6.4-1 1-1h3.5c.6 0 1 .4 1 1 0 1.3.2 2.5.6 3.6.1.3 0 .7-.2 1z"/></svg>9000000000</p>
      <p><svg width="7" height="7" viewBox="0 0 24 24"><rect x="2" y="5" width="20" height="14" fill="#ccc"/><path d="M2 5l10 8 10-8" stroke="#2b2b2b" stroke-width="2" fill="none"/></svg>hello@brightkeyhomes.net</p>
      <p><svg width="9" height="12" viewBox="0 0 24 32"><path fill="#ccc" d="M12 0a10 10 0 0 0-10 10c0 8 10 22 10 22s10-14 10-22A10 10 0 0 0 12 0zm0 14a4 4 0 1 1 0-8 4 4 0 0 1 0 8z"/></svg><span>First Floor , 42 Harbour Street<br>Seaview WA 6003</span></p>
      <div class="socials"><span></span><span></span><span></span><span></span><span></span></div>
    </div>
  </div>
  <div class="copy">Copyright © 2013 Brightkey Homes. All Rights Reserved.</div>
</footer>

</body>
</html>
```